Photography blog homepage design

I need a new webpage design for my photography blog. My blog focuses on post-processing techniques, particularly in luminosity masking, HDR photography and other advanced photo editing skills. I want the new homepage to let visitors know instantly what the blog is about as this is currently not very obvious from the feedback I received. Apart from that, the homepage should also inform/showcase latest blog post and/or popular blog post and/or some of the training courses I offer (that's my idea, but I leave it to your expertise). There should also ideally have a CTA that leads visitors to the "Start Here" page where they can learn more about my blog. The bulk of my audience is intermediate/advanced photographers who are above 30-35 years old, with a significant group in the 60 to >75 age group. The design should convey trust and creativity at the same time. The color theme for my blog is orange and dark grey. URL is www.lumbrakest.com, you can use the current content on that page.

Target Market(s)

Intermediate/advanced photographers (hobbyist or professional) age 35-75 years old.

Number of Pages Required

1 page

Font styles to use
Sans Serif

Colors
faa54b
f68e4e
f78f20

Requirements
Must have
• Upside down homepage (menus at the bottom)

```html
<!DOCTYPE html>
<html lang="en">
<head>
<meta charset="utf-8">
<title>Lumbrakest — Photography Editing Blog</title>
<link rel="stylesheet" href="https://fonts.googleapis.com/css2?family=Poppins:ital,wght@0,300;0,400;0,500;0,600;0,700;1,400&family=Dancing+Script:wght@500&display=swap">
<style>
:root{
  --orange:#f78f20;
  --orange-soft:#faa54b;
  --orange-deep:#f68e4e;
  --ink:#2b2b2b;
  --grey:#6b6b6b;
  --muted:#9a9a9a;
  --pale:#f7f7f7;
  --line:#ececec;
  --footer:#2e2e2e;
  --white:#ffffff;
}
*{margin:0;padding:0;box-sizing:border-box}
html,body{width:1200px;height:3504px;overflow:hidden}
body{font-family:'Poppins',sans-serif;color:var(--ink);background:var(--white);position:relative}
.abs{position:absolute}
section,footer{position:absolute;left:0;width:1200px}
.label{font-size:12px;letter-spacing:1px;color:var(--muted);text-transform:uppercase;text-align:center;width:100%}
.title{font-size:29px;font-weight:600;letter-spacing:2px;text-align:center;width:100%;color:var(--ink)}
.btn{position:absolute;background:var(--orange);color:#fff;font-size:12px;font-weight:600;letter-spacing:.5px;text-transform:uppercase;display:flex;align-items:center;justify-content:center;gap:8px;border-radius:2px;box-shadow:0 6px 14px rgba(247,143,32,.3)}

/* hero */
.hero{top:0;height:517px;background:var(--pale)}
.brand{left:161px;top:28px;font-size:17px;font-weight:700;letter-spacing:-.3px;color:var(--ink);display:flex;align-items:center;gap:7px}
.brand i{width:10px;height:10px;border-radius:50%;background:var(--orange);display:block}
.hero .eyebrow{left:161px;top:111px;font-size:12px;letter-spacing:1px;color:var(--muted)}
.hero h1{left:161px;top:132px;width:520px;font-size:32px;line-height:37px;font-weight:600;letter-spacing:.6px}
.hero p{left:161px;top:265px;width:510px;font-size:12.5px;line-height:23px;font-style:italic;color:#444;letter-spacing:.3px}
.polaroid{left:694px;top:54px;width:343px;height:402px;background:#f5f4f2;box-shadow:0 4px 20px rgba(0,0,0,.07)}
.polaroid .shot{left:27px;top:24px;width:286px;height:296px;background:radial-gradient(circle at 50% 45%,#d9d9d9,#b9b9b9 70%,#a7a7a7)}
.polaroid .note{left:0;width:100%;top:350px;text-align:center;font-family:'Dancing Script',cursive;font-size:17px;color:#555}

/* skills */
.skills{top:517px;height:687px;background:var(--white)}
.card{position:absolute;top:186px;width:277px;height:426px;background:#fff;border:1px solid var(--line);text-align:center}
.card.active{box-shadow:0 8px 30px rgba(0,0,0,.06)}
.card.active:before,.card.active:after{content:"";position:absolute;width:20px;height:20px;border:2px solid var(--orange-soft)}
.card.active:before{top:-2px;left:-2px;border-right:0;border-bottom:0}
.card.active:after{bottom:-2px;right:-2px;border-left:0;border-top:0}
.card .ico{position:absolute;left:101px;top:46px}
.card h3{position:absolute;top:138px;width:100%;font-size:15px;font-weight:600;letter-spacing:1.2px}
.card .rule{position:absolute;left:101px;top:188px;width:75px;height:1px;background:var(--line)}
.card.active .rule{background:var(--orange)}
.card p{position:absolute;top:213px;left:40px;width:197px;font-size:11.5px;line-height:22.5px;letter-spacing:.8px;color:#555}
.card .btn{left:47px;top:305px;width:181px;height:44px}

/* popular */
.popular{top:1204px;height:919px;background:var(--pale)}
.post{position:absolute;top:186px;width:278px}
.post .img{width:278px;height:278px;position:relative}
.post .tag{position:absolute;left:0;bottom:0;width:151px;height:45px;background:var(--orange);color:#fff;font-size:10.5px;font-weight:600;display:flex;align-items:center;justify-content:center}
.post .meta{margin-top:20px;font-size:8.5px;color:var(--orange);display:flex;gap:28px;padding-left:2px}
.post h4{margin-top:6px;font-size:13.5px;line-height:23px;font-weight:600}
.post p{margin-top:12px;font-size:11.5px;line-height:22.5px;color:#555;padding-left:2px}
.post .more{position:absolute;top:563px;left:3px;font-size:10.5px;color:var(--muted)}
.post .more.hot{color:var(--orange)}

/* latest */
.latest{top:2123px;height:425px;background:var(--white)}
.news{position:absolute;top:187px;width:300px;height:135px}
.news .img{position:absolute;left:0;top:0;width:127px;height:135px}
.news .cam{position:absolute;left:87px;top:0;width:40px;height:35px;background:var(--orange);display:flex;align-items:center;justify-content:center}
.news .txt{position:absolute;left:149px;top:12px;width:128px}
.news .date{font-size:8px;font-weight:600;letter-spacing:1px;color:var(--muted)}
.news h5{margin-top:9px;font-size:11px;line-height:15px;font-weight:600;letter-spacing:.3px}
.news p{margin-top:8px;font-size:7.5px;line-height:17px;color:#777}
.news .more{margin-top:6px;font-size:7.5px;color:var(--muted);text-align:right}
.news .more.hot{color:var(--orange)}

/* ebook */
.ebook{top:2548px;height:830px;background:var(--orange)}
.ebook .label{color:#fff;top:76px;position:absolute}
.ebook h2{position:absolute;top:94px;width:100%;text-align:center;font-size:29px;line-height:45px;font-weight:600;letter-spacing:2.5px;color:#fff}
.camera{left:163px;top:240px;width:440px;height:340px;border-radius:34px;background:linear-gradient(180deg,#3b3b3b 0%,#262626 60%,#1d1d1d 100%);box-shadow:0 30px 30px -18px rgba(0,0,0,.35)}
.perks{left:688px;top:286px;width:350px;color:#fff}
.perks h6{font-size:14px;line-height:23px;font-weight:700;letter-spacing:1.5px;color:var(--ink)}
.perks ul{list-style:none;margin-top:24px}
.perks li{display:flex;align-items:center;gap:8px;font-size:11px;letter-spacing:1px;height:37.5px}
.perks p{margin-top:12px;font-size:10px;line-height:22px;font-style:italic;color:#5a3510}
.ebook .btn{left:501px;top:694px;width:198px;height:44px;background:#fff;color:var(--orange);box-shadow:0 6px 16px rgba(0,0,0,.1)}

/* footer */
footer{top:3378px;height:126px;background:var(--footer)}
footer nav{position:absolute;top:55px;left:0;width:100%;height:20px}
footer a{position:absolute;font-size:11px;font-weight:500;color:#fff;text-decoration:none;letter-spacing:.5px}
footer a.current{color:var(--orange)}
footer a.current:before,footer a.current:after{content:"";position:absolute;width:7px;height:7px;border:1.5px solid var(--orange)}
footer a.current:before{left:-7px;bottom:-5px;border-right:0;border-top:0}
footer a.current:after{right:-7px;top:-5px;border-left:0;border-bottom:0}
</style>
</head>
<body>

<section class="hero">
  <div class="abs brand"><i></i>LUMBRAKEST</div>
  <div class="abs eyebrow">PHOTOGRAPHER</div>
  <h1 class="abs">Discover How To Be More Productive In Editing Without Spending More Time</h1>
  <p class="abs">Download the free 4-Step Editing Framework ebook. Use the KESTREL framework to boost your creativity and productivity</p>
  <a class="btn" style="left:161px;top:351px;width:200px;height:45px">Start here
    <svg width="10" height="10" viewBox="0 0 10 10"><path d="M1 5h7M5 2l3 3-3 3" stroke="#fff" stroke-width="1.4" fill="none"/></svg></a>
  <div class="abs polaroid">
    <div class="abs shot" role="img" aria-label="Black and white portrait of the blogger"></div>
    <div class="abs note">Hi, I'm Ravel</div>
  </div>
</section>

<section class="skills">
  <div class="label abs" style="top:72px">Skill wise</div>
  <div class="title abs" style="top:89px">I need help with ...</div>

  <div class="card" style="left:161px">
    <svg class="ico" width="75" height="75" viewBox="0 0 75 75"><circle cx="37.5" cy="37.5" r="36" fill="none" stroke="#8a8a8a" stroke-width="2"/><rect x="22" y="24" width="31" height="27" fill="none" stroke="#8a8a8a" stroke-width="2.5"/><rect x="28" y="30" width="19" height="15" fill="none" stroke="#8a8a8a" stroke-width="2"/><path d="M19 24h6M50 24h6M19 51h6M50 51h6" stroke="#8a8a8a" stroke-width="2"/></svg>
    <h3>Luminosity Masks</h3><div class="rule"></div>
    <p>Want to learn luminosity masking but find it too hard? Signup to the free luminosity</p>
    <a class="btn">LM crash course</a>
  </div>
  <div class="card active" style="left:460px">
    <svg class="ico" width="75" height="75" viewBox="0 0 75 75"><circle cx="37.5" cy="37.5" r="36" fill="none" stroke="#f78f20" stroke-width="2"/><path d="M21 50V26M21 50h33" stroke="#f78f20" stroke-width="2.5" fill="none"/><path d="M25 47l7-14 6 8 5-6 8 12z" fill="none" stroke="#f78f20" stroke-width="2.5" stroke-linejoin="round"/></svg>
    <h3>Histograms</h3><div class="rule"></div>
    <p>Want to learn luminosity masking but find it too hard? Signup to the free luminosity</p>
    <a class="btn">Dissecting histogram</a>
  </div>
  <div class="card" style="left:759px">
    <svg class="ico" width="75" height="75" viewBox="0 0 75 75"><circle cx="37.5" cy="37.5" r="36" fill="none" stroke="#8a8a8a" stroke-width="2"/><rect x="25" y="25" width="29" height="22" fill="none" stroke="#8a8a8a" stroke-width="2.5"/><path d="M21 29v22h29" fill="none" stroke="#8a8a8a" stroke-width="2.5"/><path d="M28 44l7-9 5 5 4-4 7 8" fill="none" stroke="#8a8a8a" stroke-width="2"/><circle cx="46" cy="31" r="2" fill="#8a8a8a"/></svg>
    <h3>Exposure Blending</h3><div class="rule"></div>
    <p>Want to learn luminosity masking but find it too hard? Signup to the free luminosity</p>
    <a class="btn">The HDR roadmap</a>
  </div>
</section>

<section class="popular">
  <div class="label abs" style="top:71px">Popular blog posts</div>
  <div class="title abs" style="top:89px">Some Of The Most Popular Blog Posts</div>

  <article class="post" style="left:162px">
    <div class="img" role="img" aria-label="Domed classical rotunda reflected in a lake at dusk" style="background:linear-gradient(180deg,#7f9cb8 0%,#a7b3bd 40%,#6d5a48 62%,#3d4a50 100%)"><div class="tag">PHOTOGRAPHY</div></div>
    <div class="meta"><span>Dec 5, 2019</span><span>Ravel</span><span>Blog,Photography</span></div>
    <h4>Creative Edit &nbsp;– &nbsp;How To Edit A Backlight Scene With Hard Selection</h4>
    <p>Backlight scene is when you take a photo with the light coming from the back of the subject. The subject can be anything from a model to a towering mountain out in the wild. It's also a of a common photography technique. You see it all the time, like in portraits! In other genre of photography, such as nature</p>
    <div class="more">READ MORE &nbsp;»</div>
  </article>
  <article class="post" style="left:462px">
    <div class="img" role="img" aria-label="Dark overhead view of a wave meeting the shore" style="background:linear-gradient(160deg,#2a2a2a 0%,#333 45%,#454545 70%,#2c2c2c 100%)">
      <svg style="position:absolute;left:122px;top:122px" width="34" height="34" viewBox="0 0 34 34"><circle cx="14" cy="14" r="10" fill="none" stroke="#f78f20" stroke-width="3"/><path d="M21 21l10 10" stroke="#f78f20" stroke-width="3.5" stroke-linecap="round"/></svg>
    </div>
    <div class="meta"><span>Dec 6, 2019</span><span>Ravel</span><span>Blog,Editcraft</span></div>
    <h4>Editcraft: How To Create More Photos Without Working Harder</h4>
    <p>Have you ever had this moment before? You come across something you've never heard before. Instead of scratching your head clueless-ly, you knew right away what it means like you have read it in a dictionary before. I happened to have a moment like this recently. Just a few days before that, I posted a photo on my</p>
    <div class="more hot">READ MORE &nbsp;»</div>
  </article>
  <article class="post" style="left:762px">
    <div class="img" role="img" aria-label="City street between tall buildings with a bridge tower at sunrise" style="background:linear-gradient(90deg,#3a3431 0%,#5b4c45 30%,#c8b4a3 50%,#6a5448 70%,#3b302c 100%)"><div class="tag">EDITCRAFT</div></div>
    <div class="meta"><span>Dec 7, 2019</span><span>Ravel</span><span>Blog, Effects</span></div>
    <h4>Creative Edit &nbsp;– &nbsp;Create Halo Effect and Directing Focus Using Lumatone</h4>
    <p>Have you ever seen photographs (typically land-scape images) where the subjects in the photo have a soft and glowing look to it? The effect is deliberate rather than a technical error by the photographer. As the matter of fact, it's called the Halo effect, named after its soft glowing look and pioneered it. If you like to read</p>
    <div class="more">READ MORE &nbsp;»</div>
  </article>

  <a class="btn" style="left:551px;top:815px;width:103px;height:29px;font-size:10px;box-shadow:none">View all</a>
</section>

<section class="latest">
  <div class="label abs" style="top:73px">Recent blog posts</div>
  <div class="title abs" style="top:91px">Some Of The Latest News Here</div>

  <article class="news" style="left:161px">
    <div class="img" role="img" aria-label="Farmhouse beside a lake under a cloudy sky" style="background:linear-gradient(180deg,#8b96a4 0%,#b2b8bd 40%,#5f6a5a 65%,#8a6a3e 100%)"></div>
    <div class="cam"><svg width="16" height="13" viewBox="0 0 16 13"><rect x="1" y="3" width="14" height="9" rx="1.5" fill="none" stroke="#fff" stroke-width="1.4"/><circle cx="8" cy="7.5" r="2.5" fill="none" stroke="#fff" stroke-width="1.4"/><path d="M5 3l1.5-2h3L11 3" fill="none" stroke="#fff" stroke-width="1.4"/></svg></div>
    <div class="txt"><div class="date">RAVEL – 10/12/2019</div><h5>How To Get Better<br>Photos While</h5><p>Backlight scene is not when you take a photo with the light coming</p><div class="more">READ MORE &nbsp;»</div></div>
  </article>
  <article class="news" style="left:461px">
    <div class="img" role="img" aria-label="Waterfall flowing over rocks at sunset" style="background:linear-gradient(180deg,#c8b69d 0%,#8d8a80 35%,#6f7b7f 60%,#4b3d33 100%)"></div>
    <div class="cam"><svg width="16" height="13" viewBox="0 0 16 13"><rect x="1" y="3" width="14" height="9" rx="1.5" fill="none" stroke="#fff" stroke-width="1.4"/><circle cx="8" cy="7.5" r="2.5" fill="none" stroke="#fff" stroke-width="1.4"/><path d="M5 3l1.5-2h3L11 3" fill="none" stroke="#fff" stroke-width="1.4"/></svg></div>
    <div class="txt"><div class="date">RAVEL – 11/12/2019</div><h5>How To Get Better<br>Photos While</h5><p>Backlight scene is when you take a photo with the light coming</p><div class="more hot">READ MORE &nbsp;»</div></div>
  </article>
  <article class="news" style="left:761px">
    <div class="img" role="img" aria-label="Gothic clock tower lit up at dusk" style="background:linear-gradient(180deg,#3e4f86 0%,#5d5e8a 45%,#6b5140 75%,#2e2a2a 100%)"></div>
    <div class="cam"><svg width="16" height="13" viewBox="0 0 16 13"><rect x="1" y="3" width="14" height="9" rx="1.5" fill="none" stroke="#fff" stroke-width="1.4"/><circle cx="8" cy="7.5" r="2.5" fill="none" stroke="#fff" stroke-width="1.4"/><path d="M5 3l1.5-2h3L11 3" fill="none" stroke="#fff" stroke-width="1.4"/></svg></div>
    <div class="txt"><div class="date">RAVEL – 12/12/2019</div><h5>How To Get Better<br>Photos While</h5><p>Backlight scene is when you take a photo with the light coming</p><div class="more">READ MORE &nbsp;»</div></div>
  </article>
</section>

<section class="ebook">
  <div class="label">E-book</div>
  <h2>Want to know how to transform images<br>like this one?</h2>
  <div class="abs camera" role="img" aria-label="DSLR camera showing a before and after edit of a frosty sunrise landscape on its screen"></div>
  <div class="abs perks">
    <h6>YOUR JOURNEY STARTS FROM NOW ON.<br>GET THE ADVANTAGES!</h6>
    <ul>
      <li><svg width="14" height="14" viewBox="0 0 14 14"><circle cx="7" cy="7" r="6" fill="none" stroke="#fff" stroke-width="1.2"/><path d="M4 7l2 2 4-4" fill="none" stroke="#fff" stroke-width="1.2"/></svg>Lorem Ipsum Dolor Amet Ningun Postedam</li>
      <li><svg width="14" height="14" viewBox="0 0 14 14"><circle cx="7" cy="7" r="6" fill="none" stroke="#fff" stroke-width="1.2"/><path d="M4 7l2 2 4-4" fill="none" stroke="#fff" stroke-width="1.2"/></svg>Lorem Ipsum Dolor Valor Dahaeris</li>
      <li><svg width="14" height="14" viewBox="0 0 14 14"><circle cx="7" cy="7" r="6" fill="none" stroke="#fff" stroke-width="1.2"/><path d="M4 7l2 2 4-4" fill="none" stroke="#fff" stroke-width="1.2"/></svg>Lorem Ipsum Dolor Simply</li>
      <li><svg width="14" height="14" viewBox="0 0 14 14"><circle cx="7" cy="7" r="6" fill="none" stroke="#fff" stroke-width="1.2"/><path d="M4 7l2 2 4-4" fill="none" stroke="#fff" stroke-width="1.2"/></svg>Lorem Ipsum Dolor Simply Dummy Text</li>
    </ul>
    <p>Dreamcatcher prism neutra shaman woke portland succulents. Health goth pickled air plant, offal XOXO kogi pour-over four dollar toast vegan hammock YOLO meh</p>
  </div>
  <a class="btn">Get free e-book
    <svg width="10" height="10" viewBox="0 0 10 10"><path d="M1 5h7M5 2l3 3-3 3" stroke="#f78f20" stroke-width="1.4" fill="none"/></svg></a>
</section>

<footer>
  <nav>
    <a class="current" style="left:430px">HOME</a>
    <a style="left:492px">START HERE</a>
    <a style="left:585px">BLOG</a>
    <a style="left:645px">TUTORIALS</a>
    <a style="left:733px">ABOUT</a>
  </nav>
</footer>

</body>
</html>
```